Fishing charter business in Sitka Alaska needs new business card design

I have had the same design for 10 plus years, ready for something different. I have attached a copy of my current card and my website link is www.tidecrestangling.example
I am looking for something that will catch my clients eye, although I rely on word of mouth for most of my business a a nice business card will help people remember who I am. My business is located in Sitka Alaska, there are probably 20-30 other charter businesses in Sitka. I like the way my current card is laid out, with the two tone black and grey. I can leave it up to the designers to come up with something else.
Target Market(s)
men, women, couples. Anyone who likes fishing
Industry/Entity Type
Tourism
Contact Information for Business Card
Dorvane's Charter Service
Kelpline Bay Sportfishing
Colors
Designer to choose colors to be used in the design.
Requirements
Must have
- Lyle Dorvane
- PO Box 4716
- Sitka, AK 99835
- Compass Rose image
- 100 Ton USCG Licensed Captain
- ldorvane@wavenet.example
- 907-555-0148
- www.tidecrestangling.example
Nice to have
- ghost image of "boat helm"
Should not have
- be to complex

```html
<!DOCTYPE html>
<html lang="en">
<head>
<meta charset="utf-8">
<title>Dorvane's Charter Service – Business Card</title>
<link href="https://fonts.googleapis.com/css2?family=Tinos:ital,wght@0,400;0,700;1,400&display=swap" rel="stylesheet">
<style>
  :root {
    --page-bg: #d9d9d9;
    --card-bg: #ffffff;
    --ink: #111111;
    --band: #000000;
    --band-text: #ffffff;
    --accent-blue: #3a55b4;
    --ghost-grey: #ebebeb;
    --rule: #222222;
    --divider: #9a9a9a;
  }
  * { margin: 0; padding: 0; box-sizing: border-box; }
  html, body {
    width: 1200px; height: 900px; overflow: hidden;
    background: var(--page-bg);
    font-family: "Tinos", "Times New Roman", serif;
    color: var(--ink);
  }
  .card {
    position: absolute; left: 100px; top: 164px;
    width: 1000px; height: 572px;
    background: var(--card-bg);
    overflow: hidden;
    box-shadow: 0 10px 30px rgba(0,0,0,0.25);
  }
  .helm-ghost {
    position: absolute; left: 70px; top: -40px;
    width: 320px; height: 320px; border-radius: 50%;
    background: var(--ghost-grey);
  }
  .compass-rose {
    position: absolute; left: 410px; top: 34px;
    width: 220px; height: 220px; border-radius: 50%;
    background: radial-gradient(circle, #1a1a1a 0%, #1a1a1a 38%, #ffffff 40%, #ffffff 62%, #4a63c0 64%, #ffffff 67%, #ffffff 84%, #111111 86%, #111111 92%, #ffffff 94%);
  }
  .brand {
    position: absolute; left: 0; right: 0; top: 268px;
    text-align: center; text-transform: uppercase;
  }
  .brand-name { font-size: 40px; font-weight: 700; letter-spacing: 1px; }
  .brand-tagline { font-size: 31px; font-weight: 400; margin-top: 2px; letter-spacing: 0.5px; }
  .rule {
    position: absolute; left: 70px; right: 40px; top: 378px;
    border-top: 2px solid var(--rule);
  }
  .contact-row {
    position: absolute; left: 70px; right: 40px; top: 396px; height: 100px;
    display: flex; align-items: center; justify-content: space-between;
  }
  .captain { flex: none; white-space: nowrap; }
  .captain-name { font-size: 26px; font-weight: 700; text-transform: uppercase; }
  .captain-title { font-size: 21px; font-style: italic; color: var(--accent-blue); margin-top: 2px; }
  .divider { flex: none; width: 2px; height: 48px; background: var(--divider); transform: skewX(-20deg); }
  .reach { flex: none; font-size: 22px; white-space: nowrap; }
  .reach-line { display: flex; align-items: center; gap: 12px; line-height: 1.4; }
  .reach-line svg { width: 20px; height: 20px; fill: var(--accent-blue); flex: none; }
  .address { flex: none; text-align: right; font-size: 23px; line-height: 1.3; white-space: nowrap; }
  .web-band {
    position: absolute; left: 0; right: 0; bottom: 0; height: 58px;
    background: var(--band); color: var(--band-text);
    display: flex; align-items: center; padding-left: 70px;
    font-size: 20px; letter-spacing: 9px; text-transform: uppercase;
  }
</style>
</head>
<body>
  <div class="card">
    <div class="helm-ghost" role="img" aria-label="Faint ghosted ship's helm wheel in light grey"></div>
    <div class="compass-rose" role="img" aria-label="Compass rose with black points inside a blue and black ring, marked N, E, S, W"></div>

    <div class="brand">
      <div class="brand-name">Dorvane's Charter Service</div>
      <div class="brand-tagline">Kelpline Bay Sportfishing</div>
    </div>

    <div class="rule"></div>

    <div class="contact-row">
      <div class="captain">
        <div class="captain-name">Lyle Dorvane</div>
        <div class="captain-title">100 Ton USCG Licensed Captain</div>
      </div>
      <div class="divider"></div>
      <div class="reach">
        <div class="reach-line">
          <svg viewBox="0 0 24 24" aria-hidden="true"><path d="M6.6 10.8a15.1 15.1 0 0 0 6.6 6.6l2.2-2.2a1 1 0 0 1 1-.25 11.4 11.4 0 0 0 3.6.57 1 1 0 0 1 1 1V20a1 1 0 0 1-1 1A17 17 0 0 1 3 4a1 1 0 0 1 1-1h3.5a1 1 0 0 1 1 1c0 1.25.2 2.450.57 3.57a1 1 0 0 1-.25 1z"/></svg>
          <span>907-555-0148</span>
        </div>
        <div class="reach-line">
          <svg viewBox="0 0 24 24" aria-hidden="true"><path d="M2 5h20v14H2z M4 7v.5l8 5 8-5V7l-8 5z" fill-rule="evenodd"/></svg>
          <span>ldorvane@wavenet.example</span>
        </div>
      </div>
      <div class="divider"></div>
      <div class="address">
        <div>PO Box 4716</div>
        <div>Sitka, AK 99835</div>
      </div>
    </div>

    <div class="web-band">www.tidecrestangling.example</div>
  </div>
</body>
</html>
```